Agricultural Commodities Specialist Needs a Business Card Design

Business owner Rob Tenwick, need a business card design for his company based in Brisbane, Australia called "RT Harvestline Pty Ltd".
Rob is an Agricultural Commodities Specialist:
-Specialising in Domestic and Export of Cotton,Cottonseed and Grains.
-Extensive experience in exporting into Asia especially China.
-Buyers agent for one of China's largest spinning mills.
-Capital raising from foreign investors into Australian agriculture.
-Agricultural marketing strategies for corporate and family farms.
-Importer of niche products from China.
-Array of contacts in agriculture and manufacturing in China.

Rob would like a professional business card with his company name "RT Harvestline" on the front of his business card - with contact details on the back. Preferably black and white colours.

CONTACT DETAILS THAT NEED TO BE INCLUDED:

Rob Tenwick
Mobile: 0437 615 249

Po Box 579
Kelvin Ridge QLD 4172

Email: rob@rtharvestline.com
website: www.rtharvestlin.com

```html
<!DOCTYPE html>
<html lang="en">
<head>
<meta charset="utf-8">
<title>RT Harvestline – Business Card Design 5</title>
<link rel="stylesheet" href="https://fonts.googleapis.com/css2?family=PT+Sans:wght@400;700&display=swap">
<style>
  :root {
    --brand-red: #ed1c24;
    --card-black: #231f20;
    --ink: #231f20;
    --paper: #ffffff;
  }
  html, body {
    margin: 0;
    padding: 0;
    width: 1000px;
    height: 1200px;
    overflow: hidden;
    background: var(--paper);
  }
  .sheet {
    position: relative;
    width: 1000px;
    height: 1200px;
    font-family: "PT Sans", sans-serif;
  }
  .sheet-title {
    position: absolute;
    top: 18px;
    left: 0;
    width: 1004px;
    margin: 0;
    text-align: center;
    font-family: "PT Sans", sans-serif;
    font-weight: 400;
    font-size: 61px;
    line-height: 72px;
    color: var(--brand-red);
  }
  .side-label {
    position: absolute;
    margin: 0;
    font-family: "PT Sans", sans-serif;
    font-weight: 400;
    font-size: 40px;
    line-height: 44px;
    color: var(--ink);
  }
  .side-label--front { left: 722px; top: 52px; }
  .side-label--back { left: 744px; top: 632px; }

  .card {
    position: absolute;
    box-sizing: border-box;
  }
  .card--front {
    left: 79px;
    top: 102px;
    width: 843px;
    height: 484px;
    background: var(--card-black);
  }
  .card--back {
    left: 77px;
    top: 680px;
    width: 847px;
    height: 488px;
    background: var(--paper);
    border: 5px solid var(--ink);
  }

  .contact {
    position: absolute;
    top: 106px;
    left: 0;
    width: 843px;
    text-align: center;
    font-family: "PT Sans", sans-serif;
    font-weight: 400;
    font-size: 20px;
    line-height: 27px;
    color: var(--paper);
  }
  .contact p { margin: 0; }
  .contact-group + .contact-group { margin-top: 27px; }
  .contact-name {
    font-weight: 700;
    font-size: 24px;
    color: var(--brand-red);
  }

  .brand-name {
    position: absolute;
    top: 207px;
    left: 0;
    width: 837px;
    margin: 0;
    text-align: center;
    font-family: "PT Sans", sans-serif;
    font-weight: 400;
    font-size: 38px;
    line-height: 44px;
    color: var(--brand-red);
  }
</style>
</head>
<body>
  <main class="sheet">
    <h1 class="sheet-title">Design-5</h1>

    <p class="side-label side-label--front">Front</p>
    <section class="card card--front" aria-label="Card front">
      <div class="contact">
        <div class="contact-group">
          <p class="contact-name">IRob Tenwick</p>
          <p>Mobile: 0437 615 249</p>
        </div>
        <div class="contact-group">
          <p>Po Box 579</p>
          <p>Kelvin Ridge QLD 4172</p>
        </div>
        <div class="contact-group">
          <p>Email: rob@rtharvestline.com</p>
          <p>website: www.rtharvestlin.com</p>
        </div>
      </div>
    </section>

    <p class="side-label side-label--back">Back</p>
    <section class="card card--back" aria-label="Card back">
      <p class="brand-name">RT Harvestline</p>
    </section>
  </main>
</body>
</html>
```